The name of my company is Tolmen Refacing LLC and I would like the sub text to say "Cabinet Refacing and Countertops". Have my name Dorian Tolmen, Owner / Sales, contact info: Cell: 360-555-0147 / Email: dorian.tolmen@quenmail.com

Simple, Clean, and Organized. With colors that will appeal to the eye.

Target Market(s)

Houses and Apartments

Industry/Entity Type

Cabinet Refacing

Contact Information for Business Card

Company name and sub text Dorian Tolmen - Owner / Sales, my cell phone number and email

Requirements
Must have
• Business name, my name / position, and my contact info
Nice to have
• Simple. Organized. Appealing to the eye

```html
<!DOCTYPE html>
<html lang="en">
<head>
<meta charset="utf-8">
<title>Tolmen Refacing LLC — Business Card</title>
<link href="https://fonts.googleapis.com/css2?family=Poppins:wght@300;400;600;700&display=swap" rel="stylesheet">
<style>
  :root {
    --page-bg: #ececec;
    --card-white: #fbfbfa;
    --ink: #161616;
    --ink-soft: #2a2a2a;
    --wood-dark: #2b2b2b;
    --wood-mid: #444444;
    --wood-light: #5a5a5a;
    --on-dark: #ffffff;
    --on-dark-soft: #e6e6e6;
  }
  * { box-sizing: border-box; margin: 0; padding: 0; }
  html, body {
    width: 1200px;
    height: 900px;
    overflow: hidden;
    background: var(--page-bg);
    font-family: "Poppins", sans-serif;
  }
  .card-sheet {
    width: 1200px;
    height: 900px;
    display: flex;
    align-items: center;
    justify-content: center;
    gap: 60px;
  }
  .card {
    position: relative;
    width: 520px;
    height: 297px;
    overflow: hidden;
    box-shadow: 0 10px 28px rgba(0,0,0,0.16);
  }

  /* Front: company side */
  .card--front { background: var(--wood-dark); color: var(--on-dark); }
  .card__texture {
    position: absolute;
    inset: 0;
    background:
      radial-gradient(ellipse at 45% 40%, rgba(255,255,255,0.10), transparent 65%),
      linear-gradient(180deg, var(--wood-mid) 0%, var(--wood-dark) 45%, var(--wood-light) 70%, var(--wood-dark) 100%);
  }
  .company {
    position: absolute;
    left: 0; right: 0;
    top: 62px;
    display: flex;
    flex-direction: column;
    align-items: center;
    text-align: center;
  }
  .company__mark {
    width: 56px;
    height: 56px;
    border-radius: 50%;
    background: var(--on-dark);
    margin-bottom: 12px;
  }
  .company__name {
    font-weight: 700;
    font-size: 33px;
    letter-spacing: 0.5px;
    text-transform: uppercase;
    line-height: 1.1;
    white-space: nowrap;
  }
  .company__tagline {
    margin-top: 4px;
    font-weight: 400;
    font-size: 17px;
    letter-spacing: 0.8px;
    color: var(--on-dark-soft);
    white-space: nowrap;
  }

  /* Back: contact side */
  .card--back { background: var(--card-white); color: var(--ink); }
  .person {
    position: absolute;
    left: 0; right: 0;
    top: 92px;
    text-align: center;
  }
  .person__name {
    font-weight: 700;
    font-size: 31px;
    letter-spacing: 4px;
    text-transform: uppercase;
    line-height: 1.1;
    white-space: nowrap;
  }
  .person__role {
    margin-top: 4px;
    font-weight: 300;
    font-size: 12px;
    letter-spacing: 5px;
    text-transform: uppercase;
    color: var(--ink-soft);
  }
  .divider {
    position: absolute;
    left: 52px; right: 52px;
    top: 190px;
    height: 1px;
    background: var(--ink);
  }
  .contact {
    position: absolute;
    left: 52px; right: 52px;
    top: 205px;
    text-align: left;
    font-weight: 400;
    font-size: 12.5px;
    letter-spacing: 0.6px;
    text-transform: uppercase;
    color: var(--ink-soft);
    white-space: nowrap;
  }
</style>
</head>
<body>
  <main class="card-sheet">
    <section class="card card--front">
      <div class="card__texture" role="img" aria-label="Dark charcoal weathered wood plank texture"></div>
      <div class="company">
        <div class="company__mark" role="img" aria-label="Company mark placeholder"></div>
        <h1 class="company__name">Tolmen Refacing, LLC</h1>
        <p class="company__tagline">Cabinet Refacing and Countertops</p>
      </div>
    </section>

    <section class="card card--back">
      <div class="person">
        <h2 class="person__name">Dorian Tolmen</h2>
        <p class="person__role">Owner / Sales</p>
      </div>
      <div class="divider"></div>
      <p class="contact">Cell: 360-555-0147 | dorian.tolmen@quenmail.com</p>
    </section>
  </main>
</body>
</html>
```